Proposal Template Design

We are looking to have our proposal templates redesigned. attached are examples of what we have been using. as well as our current logo

```html
<!DOCTYPE html>
<html lang="en">
<head>
<meta charset="utf-8">
<title>Letterhead – Summit Shield Foam</title>
<link href="https://fonts.googleapis.com/css2?family=Open+Sans:wght@400;600;700&family=Pinyon+Script&display=swap" rel="stylesheet">
<style>
  :root {
    --ink: #1f1f1f;
    --black: #161616;
    --blue: #1e88e5;
    --blue-dark: #1565c0;
    --paper: #ffffff;
    --white: #ffffff;
  }
  * { margin: 0; padding: 0; box-sizing: border-box; }
  html, body { width: 851px; height: 1200px; overflow: hidden; background: var(--paper); }
  .sheet {
    position: relative; width: 851px; height: 1200px; overflow: hidden;
    font-family: "Open Sans", Arial, sans-serif; color: var(--ink);
  }
  .decor { position: absolute; left: 0; width: 851px; }
  .decor-top { top: 0; height: 200px; }
  .decor-bottom { bottom: 0; height: 150px; }

  .brand {
    position: absolute; left: 128px; top: 62px;
    display: flex; align-items: center; gap: 10px;
  }
  .brand-mark { width: 26px; height: 26px; background: var(--blue); }
  .brand-name { font-weight: 700; font-size: 20px; color: var(--blue-dark); letter-spacing: -0.2px; }

  .services {
    position: absolute; left: 355px; top: 118px;
    font-size: 11px; font-weight: 600; color: var(--white); letter-spacing: 0.6px;
  }
  .services span + span::before { content: " | "; color: var(--blue); }

  .recipient {
    position: absolute; left: 113px; top: 333px; width: 260px;
    font-size: 14px; line-height: 20px;
  }
  .dateline { position: absolute; left: 574px; top: 427px; font-size: 14px; }

  .body {
    position: absolute; left: 113px; top: 500px; width: 630px;
    font-size: 13.6px; line-height: 19.5px;
  }
  .body p { margin-bottom: 19px; }

  .signoff { position: absolute; left: 113px; top: 978px; }
  .signature { font-family: "Pinyon Script", cursive; font-size: 42px; line-height: 46px; color: var(--ink); }
  .signer { font-size: 14px; margin-top: 2px; }

  .contact {
    position: absolute; top: 1117px; color: var(--white); font-size: 14px; line-height: 24px;
  }
  .contact-main { left: 330px; }
  .contact-address { left: 548px; }
  .contact-row { display: flex; align-items: flex-start; gap: 8px; }
  .contact-row svg { width: 13px; height: 13px; margin-top: 5px; flex: none; fill: var(--white); }
</style>
</head>
<body>
<div class="sheet">
  <svg class="decor decor-top" viewBox="0 0 851 200" aria-hidden="true">
    <path d="M0 0 H120 Q60 10 0 70 Z" fill="var(--black)"/>
    <path d="M320 100 H851 V148 H300 Z" fill="var(--black)"/>
    <path d="M300 148 L320 100 H346 L326 148 Z" fill="var(--blue)"/>
    <path d="M780 0 H851 V100 H740 Q790 60 780 0 Z" fill="var(--black)"/>
    <path d="M700 100 Q790 90 851 40 V100 Z" fill="var(--blue)"/>
  </svg>

  <div class="brand">
    <div class="brand-mark"></div>
    <div class="brand-name">Summit Shield Foam</div>
  </div>

  <div class="services"><span>SPRAY FOAM</span><span>FIBERGLASS</span><span>INSULATION</span><span>ROOFING</span></div>

  <div class="recipient">Lorem ipsum dolor sit amet, consectetuer adipiscing elit, sed tincidunt ut laoreet dolore magna enim ad minim veniam, quis nostrud exerci tation ullamcorp</div>
  <div class="dateline">Lorem ipsum dolamet,</div>

  <div class="body">
    <p>Lorem ipsum dolor sit amet, consectetuer adipiscing elit, sed diam nonummy nibh euis­mod tincidunt ut laoreet dolore magna aliquam erat volutpat. Ut wisi enim ad minim veniam, quis nostrud exerci tation ullamcorper suscipit lobortis nisl ut aliquip ex ea com­modo consequat. Duis autem vel eum iriure dolor in hendrerit in vulputate velit esse molestie praesent luptatum zzril delenit augue duis dolore te feugait nulla facilisi.</p>
    <p>Lorem ipsum dolor sit amet, cons ectetuer adipiscing elit, sed diam nonummy nibhquis nostrud exerci tation ullamcorper suscipit lobortis nisl ut aliquip ex ea commodo conse­quat.</p>
    <p>Lorem ipsum dolor sit amet, consectetuer adipiscing elit, sed diam nonummy nibh veniam, quis nostrud exerci tation ullamcorper suscipit lobortis praesent luptatum zzril delenit augue duis dolore te feugait nulla facilisi.</p>
    <p>Lorem ipsum dolor sit amet, cons ectetuer adipiscing elit, sed diam nonummy nibh veniam, quis nostrud exerci tation ullamcorper suscipit lobortis nisl ut aliquip ex ea com­modo consequat.</p>
    <p>Lorem ipsum dolor sit amet, consectetuer adipiscing elit, sed diam nonummy nibh feugiat nulla facilisis at vero eros et accumsan et iusto odio dignissim qui blandit praesent luptatum zzril delenit augue duis dolore te feugait nulla facilisi.</p>
  </div>

  <div class="signoff">
    <div class="signature">Lorem ipsum</div>
    <div class="signer">tincidunt ut laoreet</div>
  </div>

  <svg class="decor decor-bottom" viewBox="0 0 851 150" aria-hidden="true">
    <path d="M0 20 Q70 0 150 60 Q200 95 230 150 H0 Z" fill="var(--black)"/>
    <path d="M120 40 Q200 50 280 150 H240 Q200 80 120 40 Z" fill="var(--blue)"/>
    <path d="M270 45 H851 V150 H330 Q310 80 270 45 Z" fill="var(--black)"/>
    <path d="M700 150 Q760 120 851 115 V150 Z" fill="var(--blue)"/>
  </svg>

  <div class="contact contact-main">
    <div class="contact-row">
      <svg viewBox="0 0 24 24"><path d="M6.6 10.8a15 15 0 0 0 6.6 6.6l2.2-2.2a1 1 0 0 1 1-.25 11.4 11.4 0 0 0 3.6.57 1 1 0 0 1 1 1V20a1 1 0 0 1-1 1A17 17 0 0 1 3 4a1 1 0 0 1 1-1h3.5a1 1 0 0 1 1 1c0 1.25.2 2.45.57 3.57a1 1 0 0 1-.25 1z"/></svg>
      <span>555-010-2288</span>
    </div>
    <div class="contact-row">
      <svg viewBox="0 0 24 24"><path d="M2 5h20v14H2z M2 5l10 8 10-8" fill="none" stroke="#fff" stroke-width="2"/></svg>
      <span>hello@summitshieldfoam</span>
    </div>
  </div>
  <div class="contact contact-address">
    <div class="contact-row">
      <svg viewBox="0 0 24 24"><path d="M12 2a7 7 0 0 0-7 7c0 5 7 13 7 13s7-8 7-13a7 7 0 0 0-7-7zm0 9.5A2.5 2.5 0 1 1 12 6.5a2.5 2.5 0 0 1 0 5z"/></svg>
      <span>42 Linden Ave. Suite 3<br>Hartwell, TX 75000</span>
    </div>
  </div>
</div>
</body>
</html>
```